International Food Manufacturer in the need of a new business card and logo.

Our Company - Northgate Pantry Ltd.

Our Industry - Food and Drink

We are a Wild Harvested Food Distributor / Manufacturer. We service the following food sectors: Supermarkets, Hotels, Restaurants, Cafes, Catering and all people looking to eat healthy food products.

Slogan - The foremost source for everything healthy

Business card details -

48-52 Marlow Lane
Hatherby Green
London
EC9Z 4RT United Kingdom
Dennis Prowle
+44 7000 481736 - UK
+971 50 7739205 - UAE
+38 063 914 2758 - Ukraine
dennis@northgatepantry.example
www.northgatepantry.example

Goal - We are looking for a dynamic modern new look for our corporate image and a designer who can bring this new concept to our future food product designs. Please try to incorporate 3d hexagonal vector Imaging in your design concepts.

Target Market(s)

Industry/Entity Type

Food Service

Contact Information for Business Card

Northgate Pantry Ltd.
48-52 Marlow Lane
Hatherby Green
London
EC9Z 4RT United Kingdom
Dennis Prowle
+44 7000 481736 - UK
+971 50 7739205 - UAE

Font styles to use
Serif

Colors

Designer to choose colors to be used in the design.

Requirements
Must have
• Please read project description above.
Nice to have
Should not have

```html
<!DOCTYPE html>
<html lang="en">
<head>
<meta charset="utf-8">
<title>Northgate Pantry Ltd. – Business Card</title>
<link rel="stylesheet" href="https://fonts.googleapis.com/css2?family=Cinzel:wght@400;500&family=Open+Sans:wght@400&family=Arimo:wght@400&display=swap">
<style>
  :root {
    --stage: #000000;
    --paper: #ffffff;
    --leaf: #5aaa06;
    --tomato: #e3161b;
    --ink: #2a2a2a;
    --rule: #9a9a9a;
  }
  html, body {
    margin: 0;
    padding: 0;
    width: 1200px;
    height: 900px;
    overflow: hidden;
    background: var(--stage);
  }
  .canvas {
    position: relative;
    width: 1200px;
    height: 900px;
    background: var(--stage);
  }
  .card {
    position: absolute;
    width: 477px;
    height: 294px;
    box-sizing: border-box;
  }
  .card--front {
    left: 116px;
    top: 275px;
    background: var(--paper);
    border-radius: 0 62px 0 62px;
  }
  .card--back {
    left: 622px;
    top: 276px;
    height: 293px;
    background: var(--leaf);
    border-radius: 62px 0 62px 0;
  }

  /* Front */
  .brand-name {
    position: absolute;
    left: 30px;
    top: 96px;
    width: 160px;
    margin: 0;
    font-family: "Cinzel", serif;
    font-weight: 500;
    font-size: 25px;
    line-height: 1.15;
    color: var(--leaf);
    text-align: center;
  }
  .divider {
    position: absolute;
    left: 211px;
    top: 88px;
    width: 1px;
    height: 118px;
    background: var(--rule);
  }
  .person {
    position: absolute;
    left: 230px;
    top: 84px;
    margin: 0;
    font-family: "Cinzel", serif;
    font-weight: 500;
    font-size: 22px;
    letter-spacing: 0.5px;
    color: var(--leaf);
  }
  .person__surname { color: var(--tomato); }
  .contacts {
    position: absolute;
    left: 230px;
    top: 121px;
    margin: 0;
    padding: 0;
    list-style: none;
    font-family: "Open Sans", sans-serif;
    font-size: 13.5px;
    line-height: 17.5px;
    color: var(--ink);
  }
  .contacts li {
    display: flex;
    align-items: center;
    gap: 4px;
    white-space: nowrap;
  }
  .contacts .icon { width: 11px; height: 11px; flex: none; }
  .contacts .flag { width: 19px; height: 11px; flex: none; margin-left: 2px; }
  .slogan {
    position: absolute;
    left: 0;
    width: 477px;
    top: 247px;
    margin: 0;
    text-align: center;
    font-family: "Arimo", sans-serif;
    font-size: 12.5px;
    letter-spacing: 0.2px;
    color: var(--ink);
    text-transform: uppercase;
    padding-left: 0;
    transform: translateX(1px);
  }

  /* Back */
  .back-mark {
    position: absolute;
    left: 210px;
    top: 64px;
    width: 52px;
    height: 52px;
    border: 3px solid var(--paper);
    border-radius: 50%;
    box-sizing: border-box;
  }
  .company {
    position: absolute;
    left: 0;
    width: 477px;
    top: 144px;
    margin: 0;
    text-align: center;
    font-family: "Cinzel", serif;
    font-weight: 400;
    font-size: 21px;
    color: var(--paper);
  }
  .back-rule {
    position: absolute;
    left: 96px;
    top: 187px;
    width: 284px;
    height: 1px;
    background: var(--paper);
  }
  .address {
    position: absolute;
    left: 0;
    width: 477px;
    top: 205px;
    margin: 0;
    text-align: center;
    font-family: "Open Sans", sans-serif;
    font-style: normal;
    font-size: 13.5px;
    line-height: 18px;
    color: var(--paper);
  }
</style>
</head>
<body>
<main class="canvas">

  <section class="card card--front" aria-label="Business card front">
    <p class="brand-name">Northgate<br>Pantry</p>
    <span class="divider"></span>
    <h1 class="person">DENNIS <span class="person__surname">PROWLE</span></h1>
    <ul class="contacts">
      <li>
        <svg class="icon" viewBox="0 0 12 12" aria-hidden="true"><path fill="#5aaa06" d="M1 4c0-2 2-3 5-3s5 1 5 3v1H8V4H4v1H1zM3 6h6l2 5H1z"/></svg>
        +44 7000 481736
        <svg class="flag" viewBox="0 0 19 11" aria-label="UK"><rect width="19" height="11" fill="#1f3a8a"/><path d="M0 0L19 11M19 0L0 11" stroke="#fff" stroke-width="2.2"/><path d="M0 0L19 11M19 0L0 11" stroke="#d21f2b" stroke-width="0.8"/><path d="M9.5 0V11M0 5.5H19" stroke="#fff" stroke-width="3.4"/><path d="M9.5 0V11M0 5.5H19" stroke="#d21f2b" stroke-width="1.8"/></svg>
      </li>
      <li>
        <svg class="icon" viewBox="0 0 12 12" aria-hidden="true"><path fill="#5aaa06" d="M1 4c0-2 2-3 5-3s5 1 5 3v1H8V4H4v1H1zM3 6h6l2 5H1z"/></svg>
        +971 50 7739205
        <svg class="flag" viewBox="0 0 19 11" aria-label="UAE"><rect width="19" height="3.67" fill="#00843d"/><rect y="3.67" width="19" height="3.67" fill="#fff"/><rect y="7.33" width="19" height="3.67" fill="#000"/><rect width="5" height="11" fill="#e3161b"/></svg>
      </li>
      <li>
        <svg class="icon" viewBox="0 0 12 12" aria-hidden="true"><path fill="#5aaa06" d="M1 4c0-2 2-3 5-3s5 1 5 3v1H8V4H4v1H1zM3 6h6l2 5H1z"/></svg>
        +38 063 914 2758
        <svg class="flag" viewBox="0 0 19 11" aria-label="Ukraine"><rect width="19" height="5.5" fill="#1f6fd1"/><rect y="5.5" width="19" height="5.5" fill="#f7d117"/></svg>
      </li>
      <li>
        <svg class="icon" viewBox="0 0 12 12" aria-hidden="true"><rect x="1" y="2.5" width="10" height="7" fill="#5aaa06"/><path d="M1 2.5L6 6.5L11 2.5" stroke="#fff" fill="none"/></svg>
        dennis@northgatepantry.example
      </li>
      <li>
        <svg class="icon" viewBox="0 0 12 12" aria-hidden="true"><circle cx="6" cy="6" r="5" fill="#5aaa06"/><path d="M1 6H11M6 1C4 3 4 9 6 11M6 1C8 3 8 9 6 11" stroke="#fff" stroke-width="0.8" fill="none"/></svg>
        www.northgatepantry.example
      </li>
    </ul>
    <p class="slogan">The foremost source for everything healthy</p>
  </section>

  <section class="card card--back" aria-label="Business card back">
    <span class="back-mark" aria-hidden="true"></span>
    <h2 class="company">NORTHGATE PANTRY LTD.</h2>
    <span class="back-rule"></span>
    <address class="address">48-52 Marlow Lane Hatherby Green London<br>EC9Z 4RT United Kingdom</address>
  </section>

</main>
</body>
</html>
```